Brimvale Crest Homes needs a business card

We need a business card for a new company in Canada, Ontario. Our company is all about luxury contraction homes for our clients. Our product and services are custom projects design. Under the business logo that will be created, we want a slogan that will be a memorable phrase for consumers to remember us to tell their friends and relatives.

Additional infomation
- Teodoro Vanlesky
- President / Ceo
-519.304.7718

Find point what luxury construction products and services can be done

We like to see colors:
- #663300
- and something other colors or color that would attract the client needs and wants

The final design should communicate leads from new or old clients that will grow our empire. Most of all, we try to work among the budget that clients want

NOTE
- we also need an icon for the business (Example: Instagram, Facebook, and Whatsapp icons)
- We want the company name to be remembered easily for clients and our distributors who would get our orders.
- we need an icon on the business cards: Facebook and Instagram.

Thanks,
Brimvale Crest Homes

```html
<!DOCTYPE html>
<html lang="en">
<head>
<meta charset="utf-8">
<title>Brimvale Crest Homes – Business Card</title>
<link href="https://fonts.googleapis.com/css2?family=Stardos+Stencil:wght@700&family=Roboto+Condensed:wght@500&family=Ubuntu:wght@400;700&display=swap" rel="stylesheet">
<style>
  :root {
    --brown: #663300;
    --ink: #000000;
    --paper: #ffffff;
  }
  * { margin: 0; padding: 0; box-sizing: border-box; }
  html, body { width: 1200px; height: 1200px; overflow: hidden; background: var(--paper); }
  .canvas { position: relative; width: 1200px; height: 1200px; }
  .card-shapes { position: absolute; inset: 0; }
  .fill-ink { fill: var(--ink); }
  .fill-brown { fill: var(--brown); }

  .brand-name {
    position: absolute;
    font-family: "Stardos Stencil", "Arial Black", sans-serif;
    font-weight: 700;
    color: var(--brown);
    text-align: center;
    white-space: nowrap;
    line-height: 1;
  }
  .tagline {
    position: absolute;
    font-family: "Roboto Condensed", "Arial Narrow", sans-serif;
    font-weight: 500;
    color: var(--brown);
    text-align: center;
    white-space: nowrap;
    font-size: 12px;
    letter-spacing: 0.2px;
  }
  .front .brand-name { left: 232px; width: 348px; top: 544px; font-size: 29px; }
  .front .tagline { left: 232px; width: 348px; top: 579px; }
  .back .brand-name { left: 627px; width: 348px; top: 742px; font-size: 29px; }
  .back .tagline { left: 627px; width: 348px; top: 776px; }

  .back .brand-mark {
    position: absolute;
    left: 640px; width: 322px; top: 418px;
    font-family: "Stardos Stencil", "Arial Black", sans-serif;
    font-weight: 700;
    font-size: 46px;
    line-height: 1.05;
    color: var(--ink);
    text-align: center;
  }

  .contact {
    position: absolute;
    left: 321px; top: 796px;
    font-family: "Ubuntu", sans-serif;
    color: var(--brown);
    font-size: 16px;
    line-height: 1.2;
  }
  .contact .person { font-weight: 700; font-size: 15.5px; letter-spacing: 0.3px; }
  .contact .role { font-weight: 400; }
  .contact .phone { font-weight: 400; margin-top: 20px; letter-spacing: 0.5px; }

  .footer-line {
    position: absolute;
    left: 627px; width: 348px; top: 903px; height: 13px;
    font-family: "Ubuntu", sans-serif;
    font-size: 8px;
    line-height: 13px;
    color: var(--ink);
    text-align: center;
    letter-spacing: 0.2px;
  }
</style>
</head>
<body>
<div class="canvas">
  <svg class="card-shapes" width="1200" height="1200" viewBox="0 0 1200 1200" aria-hidden="true">
    <!-- front card: house silhouette -->
    <polygon class="fill-ink" points="232,291 407,291 444,328 444,306 526,306 526,411 580,464 580,916 232,916"/>
    <rect class="fill-brown" x="254" y="363" width="132" height="130"/>
    <!-- back card: upper house section -->
    <polygon class="fill-brown" points="681,306 763,306 763,328 800,291 975,291 975,632 627,632 627,464 681,411"/>
    <rect class="fill-ink" x="627" y="632" width="348" height="284"/>
    <rect class="fill-brown" x="627" y="903" width="348" height="13"/>
  </svg>

  <section class="front">
    <div class="brand-name">Brimvale Crest Homes</div>
    <div class="tagline">- HOME RENOVATIONS - CUSTOM PROJECT DESIGN -</div>
    <div class="contact">
      <div class="person">Teodoro Vanlesky</div>
      <div class="role">President / CEO</div>
      <div class="phone">519.304.7718</div>
    </div>
  </section>

  <section class="back">
    <div class="brand-mark">Brimvale Crest Homes</div>
    <div class="brand-name">Brimvale Crest Homes</div>
    <div class="tagline">- HOME RENOVATIONS - CUSTOM PROJECT DESIGN -</div>
    <div class="footer-line">GOOD HOME RENOVATION, BRIMVALE CREST HOMES</div>
  </section>
</div>
</body>
</html>
```